Corrigan's Irish Pub Menu Design

New menu design for Corrigan's Irish Pub prefer someone with menu design experience. Menu items are attached and I'll need working files to make updates. The design should be 8.5"x14" 1 cover page and 3 page menu if possible or 4 page menu if not with a Header on the first page this is for print and web. Please include the new logo and it should be in a traditional Irish Pub style. When complete please send a proof for markup (watermark is fine just want to markup and proof) and I'll send back for revisions.
Colors
Designer to choose colors to be used in the design.
Look and feel
Each slider illustrates characteristics of the customer's brand and the style your logo design should communicate.

```html
<!DOCTYPE html>
<html lang="en">
<head>
<meta charset="utf-8">
<title>Corrigan's Irish Pub – Menu</title>
<link href="https://fonts.googleapis.com/css2?family=Crimson+Text:ital,wght@0,400;0,600;0,700;1,400&display=swap" rel="stylesheet">
<style>
  :root{
    --backdrop:#eeeeec;
    --ink:#2a1f16;
    --paper-light:#f6e8cf;
    --paper-mid:#ecd2a8;
    --paper-edge:#d39a5c;
    --header:#0d0d0d;
    --header-ink:#ffffff;
    --ornament:#5a4430;
  }
  *{box-sizing:border-box;margin:0;padding:0}
  html,body{width:1200px;height:1200px;overflow:hidden}
  body{background:var(--backdrop);position:relative;font-family:"Crimson Text",Georgia,serif;color:var(--ink)}

  .page{
    position:absolute;top:297px;width:370px;height:605px;overflow:hidden;
    background:radial-gradient(ellipse 75% 70% at 50% 48%,var(--paper-light) 0%,var(--paper-mid) 62%,var(--paper-edge) 100%);
    box-shadow:0 2px 6px rgba(0,0,0,.18);
  }
  .page--cover{left:25px}
  .page--mains{left:415px}
  .page--wraps{left:805px}

  .frame-line{position:absolute;background:var(--ink)}
  .frame-line--top{top:22px;left:46px;right:46px;height:1px}
  .frame-line--bottom{bottom:22px;left:46px;right:46px;height:1px}
  .frame-line--left{left:24px;top:46px;bottom:46px;width:1px}
  .frame-line--right{right:24px;top:46px;bottom:46px;width:1px}
  .corner{position:absolute;width:22px;height:22px;background:var(--ornament);opacity:.85}
  .corner--tl{top:14px;left:16px}.corner--tr{top:14px;right:16px}
  .corner--bl{bottom:14px;left:16px}.corner--br{bottom:14px;right:16px}

  .cover-header{position:absolute;top:0;left:0;width:370px;height:165px}
  .cover-header svg{position:absolute;top:0;left:0}
  .cover-header .frame-line{background:var(--header-ink)}
  .cover-header .corner{background:#d8d8d8}
  .brand{position:absolute;top:60px;left:0;width:100%;text-align:center;color:var(--header-ink)}
  .brand__mark{display:block;width:26px;height:26px;border:1.5px solid var(--header-ink);border-radius:50%;margin:0 auto 8px}
  .brand__name{font-size:19px;font-weight:600;letter-spacing:.5px}

  .content{position:absolute;left:30px;right:30px;text-align:center;font-size:9.6px;line-height:13.6px}
  .page--cover .content{top:172px}
  .page--mains .content{top:56px}
  .page--wraps .content{top:56px}

  .menu-title{display:flex;align-items:center;justify-content:center;gap:10px;font-size:18px;letter-spacing:.5px;margin-bottom:8px}
  .menu-title .flourish{width:102px;height:6px;background:linear-gradient(90deg,transparent,var(--ink) 20%,var(--ink) 80%,transparent);opacity:.55;border-radius:3px}

  .section-title{font-size:17.5px;font-weight:600;line-height:22px;margin-bottom:6px}
  .section{margin-bottom:14px}
  .note,.desc{font-style:italic;font-size:9.2px}
  .item-name{font-weight:600}
  .item{margin-bottom:9px}
  b{font-weight:700}
</style>
</head>
<body>

<section class="page page--cover">
  <div class="cover-header">
    <svg width="370" height="165" viewBox="0 0 370 165" aria-hidden="true">
      <path d="M0 0H370V150Q185 148 0 165Z" fill="var(--header)"/>
    </svg>
    <span class="frame-line frame-line--top"></span>
    <span class="corner corner--tl" role="img" aria-label="Celtic knot corner ornament"></span>
    <span class="corner corner--tr" role="img" aria-label="Celtic knot corner ornament"></span>
    <div class="brand">
      <span class="brand__mark"></span>
      <span class="brand__name">Corrigan's Irish Pub</span>
    </div>
  </div>
  <span class="frame-line frame-line--left" style="top:50px"></span>
  <span class="frame-line frame-line--right" style="top:50px"></span>
  <span class="frame-line frame-line--bottom"></span>
  <span class="corner corner--bl" role="img" aria-label="Celtic knot corner ornament"></span>
  <span class="corner corner--br" role="img" aria-label="Celtic knot corner ornament"></span>

  <div class="content">
    <h1 class="menu-title"><span class="flourish" role="img" aria-label="Scroll flourish"></span>MENU<span class="flourish" role="img" aria-label="Scroll flourish"></span></h1>
    <div class="section">
      <h2 class="section-title">Appetizers</h2>
      <p>Irish Tacos <b>2/9-3/11</b></p>
      <p>Steak Bites <b>12 9F</b></p>
      <p>Poutine <b>13</b></p>
      <p>Irish Potato Skins <b>13</b></p>
      <p>Fish Spread <b>10</b></p>
      <p>Jalapenó Pimento Cheese Spread <b>10</b></p>
      <p>Pretzel Dippers <b>12</b></p>
      <p>Irish Nachos <b>12</b></p>
      <p>Pickle Fires <b>9</b></p>
      <p>Dunmore Gravy Fries <b>9</b></p>
      <p>Corrigans Chicken Wings <b>11</b></p>
      <p class="desc">Bear Brined Dry-rubbed and Deep Fried with your choice of:<br>Dunmore Buffalo Sauce, Whiskey Teriyaki, Corrigan's BBQ,<br>Garlic Butter, Parmesan, Grapefruit Hobanero<br>served with Celery and choice of Ranch or<br>Blue Cheese (one sauce per order)</p>
    </div>
    <div class="section">
      <h2 class="section-title">Soups and Salads</h2>
      <p class="note">Ask about the Chef's Soups: Cup <b>4</b> Bowl <b>6</b></p>
      <p>Irish Potato Salad Half <b>9</b> Full <b>12</b></p>
      <p>Garden Salad Half <b>6</b> Full <b>10</b></p>
      <p><b>Dressings:</b> Add Grilled or Blackend Chicken <b>5</b>,</p>
      <p>Add Grilled or Blackend Salad, Add Beer Tips <b>9</b>, &nbsp;Add Corned Beef</p>
    </div>
  </div>
</section>

<section class="page page--mains">
  <span class="frame-line frame-line--top"></span>
  <span class="frame-line frame-line--bottom"></span>
  <span class="frame-line frame-line--left"></span>
  <span class="frame-line frame-line--right"></span>
  <span class="corner corner--tl" role="img" aria-label="Celtic knot corner ornament"></span>
  <span class="corner corner--tr" role="img" aria-label="Celtic knot corner ornament"></span>
  <span class="corner corner--bl" role="img" aria-label="Celtic knot corner ornament"></span>
  <span class="corner corner--br" role="img" aria-label="Celtic knot corner ornament"></span>

  <div class="content">
    <div class="section">
      <h2 class="section-title">Pub Burgers</h2>
      <p class="note">Served with your choice of &nbsp;Horseradish Slaw, Mashed Potatoes</p>
      <p>The Blarney Burger &nbsp;<b>11</b></p>
      <p>The Black and Blue Burger <b>12</b></p>
      <p>The Southern Burger <b>12</b></p>
      <p>The Melt <b>12</b></p>
      <p>The Shine <b>13</b></p>
    </div>
    <div class="section">
      <h2 class="section-title">Pub Sandwishes</h2>
      <p>Revbew <b>12</b></p>
      <p>Rachel <b>12</b></p>
      <p>Classic Grilled Chicken <b>12</b></p>
      <p>The Celtic Chicken <b>11</b></p>
      <p>The Corrigan <b>13</b></p>
      <p>Grilled Pimento Cheese <b>11</b></p>
      <p>Veggie Burger <b>11</b></p>
      <p class="item-name">The Big Turkey 12</p>
      <p class="desc">Smoke Turkey, Apple Wood, Bacon, Swiss Cheese, Lettuce,<br>Tomato, Red Onion of Cajun Ranch on Grilled Sourdough</p>
      <p class="item-name">Salmon Blt 13</p>
      <p class="desc">Grill Salmon, Applewood, Bacon, Lettuce, Tomato and<br>Roasted Garlic and Thyme on Grilled Sourdough</p>
      <p class="item-name">BBQ Pork 12</p>
      <p class="desc">Pulled Pork, Cole Slaw, Pickles and Corrigan's<br>BBQ Sauce on a Potato Roll</p>
    </div>
    <div class="section">
      <h2 class="section-title">Wraps</h2>
      <div class="item">
        <p class="item-name">The Chicken Wrap 12</p>
        <p class="desc">Grilled or Blackend Chicken, Lettuce, Tomatoes,<br>Red Onion, Applewood Bacon and Parmeson Ranch</p>
      </div>
      <div class="item">
        <p class="item-name">The Turkey Wrap 12</p>
        <p class="desc">Smoked Turkey Swiss Cheese, Spinach, Tomato,<br>Applewood Bacon and Cranberry Aioli</p>
      </div>
    </div>
  </div>
</section>

<section class="page page--wraps">
  <span class="frame-line frame-line--top"></span>
  <span class="frame-line frame-line--bottom"></span>
  <span class="frame-line frame-line--left"></span>
  <span class="frame-line frame-line--right"></span>
  <span class="corner corner--tl" role="img" aria-label="Celtic knot corner ornament"></span>
  <span class="corner corner--tr" role="img" aria-label="Celtic knot corner ornament"></span>
  <span class="corner corner--bl" role="img" aria-label="Celtic knot corner ornament"></span>
  <span class="corner corner--br" role="img" aria-label="Celtic knot corner ornament"></span>

  <div class="content">
    <div class="item">
      <p class="item-name">The Haddock Wrap 13</p>
      <p class="desc">Grilled or Blackend Haddock, Lettuce, Tomato,<br>Cheddar Cheese amd Removlade</p>
    </div>
    <div class="item">
      <p class="item-name">The Salmon Wrap 13</p>
      <p class="desc">Grilled or Blackend Salmon, Spinach, Tomato, Scallions,<br>Gouda Cheese and Garlic and Thyme Aioli</p>
    </div>
    <div class="item">
      <p class="item-name">The Veggie Wrap 12</p>
      <p class="desc">Artichokes, Spinach, toamto, Cucumbers, Red Onion,<br>Mozzarella Cheese and a Roasted Red Pepper Aioli<br>10" Flat Breads with Gluten Free Cauliflower Crust</p>
    </div>
    <div class="item">
      <p class="item-name">BBQ Pork 12</p>
      <p class="desc">Corrigan's BBQ Sauce, Pulled Mojo Pork, Sliced Apples,<br>Blue Cheese, Crumbbles and Mozzarella Cheese</p>
    </div>
    <div class="item">
      <p class="item-name">Buffalo Chicken 12</p>
      <p class="desc">Dunmore Buffalo Sauce, Pulled Chicken, Diced Celery,<br>Scallions, Blue Cheese, Crumbles and Mozzarella Cheese</p>
    </div>
    <div class="item">
      <p class="item-name">Irish Banger12</p>
      <p class="desc">Stout Grain Mustard Sauce, Bangers, Applewood Bacon,<br>Roasted Red Pepper and Smoked Gouda Cheese</p>
    </div>
    <div class="item" style="margin-bottom:18px">
      <p class="item-name">Veggie Pie 12</p>
      <p class="desc">Whisked Fig Cream Cheese Sauce, Spinach, Artichokes, Celery, Tomatoes,<br>Cucumber, Scallions, Parmesan and Smoked Gouda Cheese.</p>
    </div>
    <div class="section">
      <h2 class="section-title">Entreés</h2>
      <p>Bangers and Mash <b>15</b></p>
      <p>Shepherd's Pie <b>13</b></p>
      <p>Fish and Chips <b>13</b></p>
      <p class="item-name" style="margin-top:3px">Corned Beef and Cabbage 13</p>
      <p class="desc">Dunmore Pulled Corned Beef with Caraway Cabbage and<br>Smoked Gouda, Mashed Potatoes, Served with Stout Mustard</p>
      <p>Gaelic Breakfast Plate <b>12</b></p>
    </div>
  </div>
</section>

</body>
</html>
```